RESIDENCE VALBRUNE

The CORVALE Immobilier company exclusively offers apartments for sale under a tax exemption law (BELTRAVIGNE) in CAMBRAI, 92 apartments are available, fully renovated with balcony, terrace, elevator, in a former military residence known to the city.
We want to make a book to give to our customers.

```html
<!DOCTYPE html>
<html lang="fr">
<head>
<meta charset="utf-8">
<title>Résidence Valbrune – CORVALE Immobilier</title>
<link href="https://fonts.googleapis.com/css2?family=Open+Sans:wght@400;600;700&display=swap" rel="stylesheet">
<style>
:root{
  --bg:#e4e4e4;
  --paper:#ffffff;
  --gold:#c9974a;
  --gold-soft:#ecdcc0;
  --ink:#3a3a3a;
  --ink-soft:#555555;
  --rule:#d8c29c;
  --render-a:#c3d2de;
  --render-b:#b59a8a;
}
*{box-sizing:border-box;margin:0;padding:0}
html,body{width:1200px;height:800px;overflow:hidden;background:var(--bg)}
body{font-family:"Open Sans",Arial,sans-serif;color:var(--ink)}
.spread{position:absolute;left:40px;top:120px;width:1120px;height:560px;display:flex;box-shadow:0 10px 30px rgba(0,0,0,.18)}
.page{width:560px;height:560px;position:relative;background:var(--paper);overflow:hidden}
.page--left .hero{position:absolute;inset:0;background:linear-gradient(170deg,var(--render-a) 0%,var(--render-b) 100%)}
.brand-tile{position:absolute;right:28px;bottom:40px;width:108px;height:108px;background:var(--paper);display:flex;flex-direction:column;align-items:center;justify-content:center;gap:6px}
.brand-tile .mark{width:18px;height:18px;background:var(--gold)}
.brand-tile .name{font-weight:600;font-size:10px;letter-spacing:.08em;color:var(--gold);text-align:center;line-height:1.3}
.page--right{padding:26px 24px 20px 26px;display:grid;grid-template-columns:repeat(4,1fr);grid-template-rows:auto 1fr;column-gap:12px;row-gap:10px;border-left:1px solid #ddd}
.lead{grid-column:1/3}
.title{font-weight:600;font-size:17px;line-height:1.25;color:var(--gold);padding-top:58px;margin-bottom:10px}
.intro{font-weight:700;font-size:8.3px;line-height:1.45;color:var(--ink);text-align:justify;padding-bottom:8px;border-bottom:1px solid var(--rule)}
.visual{grid-column:3/5;height:170px;border:3px solid var(--gold-soft);box-shadow:0 1px 4px rgba(0,0,0,.15);background:linear-gradient(170deg,var(--render-a) 0%,var(--render-b) 100%)}
.col{font-size:7px;line-height:1.5;color:var(--ink-soft);text-align:justify}
.col p{margin-bottom:5px}
.col h3{font-size:7.4px;font-weight:600;color:var(--gold);line-height:1.35;margin-bottom:4px}
.offer{font-weight:700;color:var(--ink);font-size:7.4px;margin:6px 0}
.contact{background:var(--gold-soft);padding:6px 8px;font-size:7px;font-weight:600;color:var(--gold);line-height:1.5}
</style>
</head>
<body>
<main class="spread">
  <section class="page page--left">
    <div class="hero" role="img" aria-label="Vue 3D de la résidence rénovée : immeubles en brique et façades blanches le long d'une rue arborée"></div>
    <div class="brand-tile">
      <span class="mark"></span>
      <span class="name">CORVALE<br>Immobilier</span>
    </div>
  </section>

  <section class="page page--right">
    <header class="lead">
      <h1 class="title">La résidence Valbrune à CAMBRAI devient la résidence ALCYONE</h1>
      <p class="intro">Le GROUPE CORVALE Immobilier vous propose de réaliser un investissement locatif clefs en main en BELTRAVIGNE ; le spécialiste de l'investissement immobilier se lance dans un programme ambitieux avec la rénovation d'une ancienne caserne militaire à Cambrai. Éligible au dispositif, cette opération offre une opportunité unique aux primo-investisseurs.</p>
    </header>
    <div class="visual" role="img" aria-label="Perspective de la résidence rénovée avec jardins et parking"></div>

    <div class="col">
      <p>L'ancienne résidence militaire Valbrune va faire peau neuve et se transformer en résidence de standing ! Souhaitant conserver l'historique des lieux, elle portera le nom d'ALCYONE. Les 3 bâtiments seront baptisés en souvenir de l'armée française.</p>
      <p>Cette résidence construite en 1958, située à deux pas du centre-ville et du quartier Saint Aubert, est en pleine rénovation. 92 logements de standing y sont proposés à partir de 125.000 euros, les premiers seront livrés en 2023 !</p>
      <p>C'est un projet titanesque, dont le promoteur lillois s'est lancé comme défi de rénover l'ensemble : les parties communes, les façades extérieures, les toitures et les espaces communs. Les 3 bâtiments seront habitables d'ici la fin de l'année 2025, et le premier bâtiment baptisé « Horizon » sera le premier à héberger les locataires ou propriétaires.</p>
    </div>
    <div class="col">
      <h3>Le promoteur a choisi d'allier LE GROUPE CORVALE Immobilier à sa cause</h3>
      <p>Reconnu pour son savoir-faire en matière d'investissement locatif à Cambrai, LE GROUPE CORVALE IMMOBILIER se lance en co-promotion et la commercialisation exclusive d'un nouveau projet : la rénovation d'une ancienne résidence militaire. « Les bâtiments ont été très bien conçus, ce qui nous offre la possibilité de réaliser des produits de qualité avec des ascenseurs, des balcons, des rez-de-jardin, des caves et même quelques places de parking » détaille Marc Delorme.</p>
      <p>« La résidence est éligible au dispositif BELTRAVIGNE, CAMBRAI est l'une des villes exclusives à bénéficier de cette aide fiscale. C'est une véritable opportunité puisque le dispositif doit s'achever le 31 décembre 2022 » souligne-t-il.</p>
    </div>
    <div class="col">
      <h3>Une véritable opportunité !</h3>
      <p>Le dispositif BELTRAVIGNE offre la possibilité aux particuliers acquéreurs d'un appartement ancien dans un but locatif de bénéficier d'une réduction d'impôt sur le revenu pouvant aller jusqu'à 6.000 euros par an. Seule contrainte : louer le logement non meublé comme résidence principale pendant 6, 9 ou 12 ans.</p>
      <p>« Nous proposons une opération clé en main puisque c'est le promoteur qui réalise les travaux et que nous pouvons accompagner les investisseurs dans le financement de leur bien mais aussi assurer la gestion locative » explique Marc Delorme.</p>
      <p>Ce programme est une occasion inédite pour les primo-investisseurs de se constituer un premier patrimoine immobilier sans apport et financé entièrement.</p>
    </div>
    <div class="col">
      <p>« grâce au loyer perçu » ajoute-t-il, rappelant que LE GROUPE CORVALE propose une assurance 100% garantie loyer impayé, sans délais de carence et en paiement immédiat. « L'immobilier demeure un investissement de choix, c'est une valeur sûre et il est possible de revendre son bien à tout moment » souligne Marc Delorme.</p>
      <p>Le GROUPE CORVALE Immobilier est à votre disposition pour vous recevoir et vous fournir toutes les informations sur cette nouvelle résidence et vous établir une étude fiscale personnalisée.</p>
      <p class="offer">Pour toute réservation d'un logement d'ici le 30 juin, les frais de Notaires sont offerts !</p>
      <div class="contact">Groupe CORVALE IMMOBILIER<br>14 RUE DES TILLEULS<br>59400 Cambrai<br>03 27 45 18 60</div>
    </div>
  </section>
</main>
</body>
</html>
```